Broschüren-Design für Versicherungsagenten
Zielgruppe
Ich bin mit KL-Vorsorge als unabhängiger Versicherungsagent Selbstständig. (www.kl-vorsorge.de)
Ich habe mich auf die Absicherung von biometrischen Risiken spezialisiert - die auch in der Broschüre Thematisiert werden sollen. Das Oberthema der Broschüre ist 'biometrische Risiken'. Dies soll dann auf die Themen: Arbeitskraft, Langlebigkeit und Pflege heruntergebrochen werden.
Zielgruppe sind vor allem junge Menschen, die gerade erst eine Ausbildung gestartet oder ihr Studium beendet haben.
Aufgabenstellung
Das Design sollte die drei Hauptbereiche: Arbeitskraft, Langlebigkeit und Pflege, leicht verständlich dem Kunden veranschaulichen. Texte, Informationen und Grafiken (in der Reihenfolge, so wie ich mir das vorstelle) sind als Datei beigefügt.
Das ganze soll im DIN A4 Format gedruckt werden, wobei ich auf einen Hochwertigen Druck inklusive Druckveredelung hohen Wert lege.

```html
<!DOCTYPE html>
<html lang="de">
<head>
<meta charset="utf-8">
<title>Broschüre – Arbeitskraft</title>
<link rel="stylesheet" href="https://fonts.googleapis.com/css2?family=Montserrat:wght@300;400;500&family=Share+Tech+Mono&display=swap">
<style>
  :root {
    --backdrop: #e4e4e4;
    --page: #f1f1ef;
    --panel-light: #f4f4f2;
    --panel-warm: #ebe7de;
    --accent: #e9ac63;
    --ink: #2b2b2b;
    --muted: #6d6d6d;
    --icon-grey: #9a9a9a;
    --chip: #d9d6cf;
  }
  * { box-sizing: border-box; margin: 0; padding: 0; }
  html, body { width: 1200px; height: 857px; overflow: hidden; }
  body {
    background: var(--backdrop);
    font-family: "Montserrat", sans-serif;
    color: var(--ink);
    position: relative;
  }
  .spread {
    position: absolute;
    left: 40px; top: 230px;
    width: 1120px; height: 396px;
    display: flex;
    box-shadow: 0 6px 24px rgba(0,0,0,.12);
  }
  .page { position: relative; width: 560px; height: 396px; overflow: hidden; }
  .page--photo { background: var(--page); }
  .photo-area {
    position: absolute; inset: 0;
    background: linear-gradient(120deg, #8c8c8a 0%, #c9c8c5 35%, #e6e5e2 60%, #f4f3f1 100%);
  }
  .title-label {
    position: absolute;
    left: 350px; top: 250px;
    width: 210px; height: 78px;
    background: var(--accent);
    padding: 16px 18px;
  }
  .title-label__kicker { font-size: 12px; font-weight: 400; color: var(--ink); }
  .title-label__main {
    font-family: "Share Tech Mono", monospace;
    font-size: 22px; letter-spacing: 4px; margin-top: 4px;
  }
  .page--facts {
    background: var(--page);
    display: flex; gap: 14px;
    padding: 18px 20px 18px 24px;
  }
  .panel { flex: 1; padding: 26px 22px; position: relative; }
  .panel--stat { background: var(--panel-light); text-align: center; }
  .panel--value { background: var(--panel-warm); text-align: center; }
  .panel__heading {
    font-family: "Share Tech Mono", monospace;
    font-size: 20px; letter-spacing: 3px; color: var(--ink);
  }
  .panel__text {
    font-size: 9px; font-weight: 300; line-height: 1.5;
    color: var(--muted); margin: 14px auto 0; max-width: 190px;
  }
  .people { display: flex; justify-content: center; gap: 14px; margin-top: 36px; }
  .people svg { width: 28px; height: 64px; }
  .panel__question {
    font-size: 12px; font-weight: 400; line-height: 1.5;
    margin-top: 36px; color: var(--ink);
  }
  .highlight { color: var(--accent); }
  .formula {
    display: grid;
    grid-template-columns: 1fr auto 1fr;
    align-items: center; gap: 6px 8px;
    margin-top: 34px; text-align: left;
  }
  .formula__stack { display: flex; flex-direction: column; align-items: flex-start; gap: 4px; }
  .chip {
    background: var(--chip); font-size: 7px; padding: 3px 6px;
    border-radius: 2px; color: var(--ink);
  }
  .op { font-size: 8px; color: var(--muted); padding-left: 10px; }
  .page-number {
    position: absolute; right: 8px; bottom: 10px;
    font-size: 7px; color: var(--muted);
  }
</style>
</head>
<body>
  <main class="spread">
    <section class="page page--photo">
      <div class="photo-area" role="img" aria-label="Schwarzweißfoto: junge Menschen im Gespräch, lächelnd"></div>
      <div class="title-label">
        <p class="title-label__kicker">Ihr größtes Vermögen</p>
        <h1 class="title-label__main">ARBEITSKRAFT »</h1>
      </div>
    </section>

    <section class="page page--facts">
      <article class="panel panel--stat">
        <h2 class="panel__heading">1 VON 4</h2>
        <p class="panel__text">Einer von 4 Menschen kann im Laufe seines Lebens seinen ursprünglichen Beruf aus gesundheitlichen Gründen nicht mehr ausüben</p>
        <div class="people" aria-label="Vier Personen, eine hervorgehoben">
          <svg viewBox="0 0 28 64"><circle cx="14" cy="7" r="6" fill="var(--icon-grey)"/><rect x="4" y="15" width="20" height="24" rx="3" fill="var(--icon-grey)"/><rect x="7" y="38" width="6" height="24" fill="var(--icon-grey)"/><rect x="15" y="38" width="6" height="24" fill="var(--icon-grey)"/></svg>
          <svg viewBox="0 0 28 64"><circle cx="14" cy="7" r="6" fill="var(--icon-grey)"/><rect x="4" y="15" width="20" height="24" rx="3" fill="var(--icon-grey)"/><rect x="7" y="38" width="6" height="24" fill="var(--icon-grey)"/><rect x="15" y="38" width="6" height="24" fill="var(--icon-grey)"/></svg>
          <svg viewBox="0 0 28 64"><circle cx="14" cy="7" r="6" fill="var(--accent)"/><rect x="4" y="15" width="20" height="24" rx="3" fill="var(--accent)"/><rect x="7" y="38" width="6" height="24" fill="var(--accent)"/><rect x="15" y="38" width="6" height="24" fill="var(--accent)"/></svg>
          <svg viewBox="0 0 28 64"><circle cx="14" cy="7" r="6" fill="var(--icon-grey)"/><rect x="4" y="15" width="20" height="24" rx="3" fill="var(--icon-grey)"/><rect x="7" y="38" width="6" height="24" fill="var(--icon-grey)"/><rect x="15" y="38" width="6" height="24" fill="var(--icon-grey)"/></svg>
        </div>
        <p class="panel__question">Können Sie wissen ob<br>Sie einer der anderen drei<br>oder der <span class="highlight">EINE</span> sind?</p>
      </article>

      <article class="panel panel--value">
        <h2 class="panel__heading">1.500.000 €</h2>
        <p class="panel__text">Im Laufe eines Arbeitslebens verdient ein durchschnittlicher Erwerbstätiger rund 1,5 Millionen Euro</p>
        <div class="formula">
          <div class="formula__stack">
            <span class="chip">Einkommen</span>
            <span class="op">×</span>
            <span class="chip">12 Monate</span>
            <span class="op">×</span>
            <span class="chip">Arbeitsjahre bis Renteneintritt</span>
          </div>
          <span class="op">=</span>
          <span class="chip">Wert Ihrer Arbeitskraft</span>
        </div>
        <p class="panel__question">Wie viel ist Ihre<br><span class="highlight">Arbeitskraft</span> wert?</p>
        <span class="page-number">4</span>
      </article>
    </section>
  </main>
</body>
</html>
```